Ferris Contracting LLC Business Card Design

I am looking for a creative and unique business card design. We are a commercial construction general contractor. With the name "FERRIS" Contracting, I am hoping to see some neat designs that correlate with the name.

```html
<!DOCTYPE html>
<html lang="en">
<head>
<meta charset="UTF-8">
<title>Ferris Contracting LLC – Business Card</title>
<link href="https://fonts.googleapis.com/css2?family=Open+Sans:wght@400;600;800&display=swap" rel="stylesheet">
<style>
  :root {
    --backdrop: #dfe1e3;
    --card-white: #ffffff;
    --blue-deep: #1d4f8c;
    --blue-mid: #5f8fc2;
    --blue-pale: #dbe6f1;
    --logo-blue: #1f7cc4;
    --ink: #4a4f57;
    --ink-soft: #6c727a;
    --on-blue: #ffffff;
  }
  * { box-sizing: border-box; margin: 0; padding: 0; }
  html, body {
    width: 1200px;
    height: 686px;
    overflow: hidden;
    background: var(--backdrop);
    font-family: "Open Sans", Arial, sans-serif;
  }
  .card {
    position: absolute;
    left: 75px;
    top: 43px;
    width: 1050px;
    height: 600px;
    border-radius: 28px;
    overflow: hidden;
    background: linear-gradient(100deg,
      var(--card-white) 0%,
      var(--card-white) 44%,
      var(--blue-pale) 56%,
      var(--blue-mid) 76%,
      var(--blue-deep) 100%);
    box-shadow: 0 14px 30px rgba(0, 0, 0, 0.18);
  }
  .card__backdrop-ring {
    position: absolute;
    left: 520px;
    top: 90px;
    width: 520px;
    height: 520px;
  }
  .brand {
    position: absolute;
    left: 190px;
    top: 190px;
    display: flex;
    align-items: center;
    gap: 18px;
  }
  .brand__dot {
    width: 46px;
    height: 46px;
    border-radius: 50%;
    background: var(--logo-blue);
  }
  .brand__name {
    font-weight: 800;
    font-size: 78px;
    letter-spacing: 1px;
    color: var(--logo-blue);
    line-height: 1;
  }
  .contact {
    position: absolute;
    left: 210px;
    top: 330px;
    width: 400px;
    text-align: center;
    color: var(--ink-soft);
    font-size: 26px;
    line-height: 1.3;
  }
  .contact__name {
    font-weight: 600;
    font-size: 30px;
    color: var(--ink);
  }
  .services {
    position: absolute;
    right: 60px;
    top: 50px;
    text-align: right;
    color: var(--on-blue);
  }
  .services__brand {
    font-weight: 800;
    font-size: 46px;
    letter-spacing: 1px;
    line-height: 1;
  }
  .services__tag {
    font-weight: 600;
    font-size: 17px;
    letter-spacing: 7px;
    margin-top: 6px;
    opacity: 0.9;
  }
  .services__list {
    list-style: none;
    margin-top: 14px;
    font-size: 19px;
    line-height: 1.3;
  }
</style>
</head>
<body>
  <div class="card">
    <svg class="card__backdrop-ring" viewBox="0 0 520 520" aria-hidden="true">
      <circle cx="260" cy="260" r="220" fill="none" stroke="#ffffff" stroke-opacity="0.16" stroke-width="40"/>
    </svg>

    <div class="brand">
      <span class="brand__dot"></span>
      <span class="brand__name">FERRIS</span>
    </div>

    <div class="contact">
      <p class="contact__name">Daniel Harlow</p>
      <p>Owner/Operator</p>
      <p>555-214-7830</p>
      <p>info@ferriscontracting.com</p>
      <p>www.ferriscontracting.com</p>
    </div>

    <div class="services">
      <p class="services__brand">FERRIS</p>
      <p class="services__tag">CONTRACTING</p>
      <ul class="services__list">
        <li>Residential &amp; Commercial</li>
        <li>Demolition</li>
        <li>Excavation</li>
        <li>Renovations</li>
        <li>Decking &amp; Fencing</li>
      </ul>
    </div>
  </div>
</body>
</html>
```